Grins of Pellbrook - Dental, needs a redesign

Purpose:
Redesign website: http://www.grinsofpellbrook.example/

Sections are important, but for content, we can use existing website or have some placeholder text to fill in later.

Some of the required sections:
About us, contact us, services, our offices, our staff, patient education, patient forms (link to Molavex can be used here), link to friendspace, testimonials

Editability:
We would like to be able to update and edit the content in the future, for small changes

Pictures:
Here is a link to the staff pictures we’d like to use on the website:
https://www.filecrate.example/sh/493kq7zz2tt118p5/BBDRmwLe_uKPi8ZrafQWTGeeb?dl=0
You don't have to use all the pictures; just a few.

friendspace page:
https://www.friendspace.example/Grins-of-Pellbrook-627150384019562

Colors: Calming colors/images for a soothing feeling... to assure the patient that it'll not be that bad.

Target Market(s)

General population

Industry/Entity Type

Dental Clinic

Coding

Coded - Design and coding required

Number of Pages Required

5+ page

Requirements
Must have
• About us, contact us, services, our offices, our staff, patient education, patient forms (link to Molavex can be used here), link to friendspace, testimonials.
• Just create the placeholders for content or use from existing website.
• The staff picture of everyone needs to be on the home page - because that makes it more personal and has received positive feedback from many patients.

```html
<!DOCTYPE html>
<html lang="en">
<head>
<meta charset="utf-8">
<title>Grins of Pellbrook - Dental</title>
<link rel="stylesheet" href="https://fonts.googleapis.com/css2?family=Roboto:wght@300;400;500;700&display=swap">
<style>
:root{
  --teal:#1fc8c9;
  --teal-deep:#19b9bf;
  --purple:#6a2ff2;
  --purple-soft:#7b45f0;
  --ink:#3a3a3a;
  --muted:#555;
  --white:#fff;
  --line:#e3e3e3;
}
*{box-sizing:border-box;margin:0;padding:0}
html,body{width:1200px;height:2442px;overflow:hidden}
body{position:relative;font-family:"Roboto",Helvetica,Arial,sans-serif;color:var(--ink);background:var(--white);font-weight:300}
.abs{position:absolute}

/* top bar */
.topbar{left:0;top:0;width:1200px;height:37px;background:var(--teal);color:var(--white);font-size:13px;font-weight:400}
.topbar .info{left:166px;top:10px;display:flex;gap:22px;align-items:center}
.topbar .info span{display:flex;align-items:center;gap:6px}
.topbar .social{right:121px;top:10px;display:flex;gap:10px;font-size:12px}

/* header */
.header{left:0;top:37px;width:1200px;height:81px;border-bottom:1px solid var(--line)}
.brand{left:166px;top:22px;display:flex;align-items:center;gap:12px}
.brand-dot{width:34px;height:34px;border-radius:50%;background:var(--purple-soft)}
.brand-name{font-size:25px;font-weight:400;color:var(--teal)}
.phone{right:121px;top:27px;display:flex;align-items:center;gap:10px;font-size:20px;color:var(--teal);font-weight:300}

/* nav */
.nav{left:166px;top:119px;height:60px;display:flex;align-items:stretch}
.nav a{display:flex;align-items:center;font-size:17px;color:#333;text-decoration:none;font-weight:300;text-transform:uppercase;padding:0 13px;margin-right:13px}
.nav a.active{background:var(--teal);color:var(--white);font-weight:500;padding:0 12px;margin-right:15px}

/* hero */
.hero{left:0;top:179px;width:1200px;height:475px;background:linear-gradient(180deg,#29c6d6 0%,#4f8deb 45%,#7a3ff0 100%);overflow:hidden}
.hero-photo{left:610px;top:0;width:497px;height:475px;background:linear-gradient(180deg,rgba(255,255,255,.28),rgba(255,255,255,.12));}
.hero-kicker{left:166px;top:77px;font-size:27px;color:var(--white);font-weight:300}
.hero-line{left:166px;width:368px;height:53px;background:rgba(255,255,255,.35);color:var(--white);font-size:44px;font-weight:300;padding-left:16px;line-height:53px;white-space:nowrap}
.hero-line strong{font-weight:700}
.btn{position:absolute;height:39px;border-radius:20px;font-size:21px;display:flex;align-items:center;justify-content:center;font-weight:400}
.btn-solid{left:166px;top:295px;width:156px;background:var(--white);color:var(--purple)}
.btn-ghost{left:355px;top:295px;width:156px;border:2px solid var(--white);color:var(--white)}
.dots{display:flex;gap:12px}
.dot{width:12px;height:12px;border-radius:50%;border:2px solid var(--white)}
.dot.on{background:var(--white)}

/* sections */
.section-title{width:1200px;left:0;text-align:center;font-size:38px;font-weight:300}
.section-title strong{font-weight:500}
.section-sub{width:1200px;left:0;text-align:center;font-size:17px;color:#333;font-weight:300}
.why-title{top:718px;color:var(--purple)}
.why-sub{top:776px}
.feature{top:858px;width:220px;text-align:center;font-size:17px;line-height:24px;color:#444}
.feature svg{display:block;margin:0 auto 18px;width:60px;height:62px}

/* doctor */
.doctor{left:0;top:1066px;width:1200px;height:427px;background:linear-gradient(90deg,#22c8cf 0%,#45a8e2 45%,#6a3ff2 100%)}
.doctor-photo{left:147px;top:33px;width:268px;height:394px;background:linear-gradient(180deg,rgba(40,40,60,.25),rgba(20,20,40,.55))}
.doctor-title{left:451px;top:72px;font-size:38px;color:var(--white);font-weight:300}
.doctor-title strong{font-weight:500}
.doctor-text{left:451px;top:136px;width:590px;font-size:15.5px;line-height:23.6px;color:var(--white);font-weight:300}
.doctor-text p+p{margin-top:23px}
.btn-team{left:451px;top:305px;width:303px;border:2px solid var(--white);color:var(--white)}

/* testimonials */
.happy-title{top:1568px;color:var(--teal)}
.happy-sub{top:1624px}
.quote{top:1700px;width:400px;height:229px;text-align:center;padding:18px 30px 0}
.quote-mark{font-size:30px;font-weight:700;line-height:26px}
.quote p{font-size:14.5px;line-height:21px;margin-top:6px}
.quote .who{display:flex;align-items:center;justify-content:center;gap:20px;margin-top:22px;text-align:left}
.avatar{width:67px;height:67px;border-radius:50%;background:linear-gradient(180deg,#d9c3a8,#a88c74)}
.who b{display:block;font-size:15px;font-weight:500;letter-spacing:.3px}
.who small{font-size:12.5px}
.quote-purple{left:166px;background:var(--purple);color:var(--white)}
.quote-outline{left:633px;border:2.5px solid var(--teal);color:#555}
.quote-outline .quote-mark{color:#333}
.happy-dots{left:557px;top:1981px;gap:20px}
.happy-dots .dot{width:17px;height:17px;border-color:var(--teal)}
.happy-dots .dot.on{background:var(--teal)}

/* footer */
.hours{left:0;top:2061px;width:600px;height:381px;background:var(--teal);color:var(--white)}
.contact{left:600px;top:2061px;width:600px;height:381px;background:var(--purple);color:var(--white)}
.foot-title{top:45px;font-size:28px;font-weight:300}
.foot-title strong{font-weight:500}
.hours .foot-title{left:164px}
.hours-table{left:164px;top:96px;width:304px;border-collapse:collapse;font-size:16.5px}
.hours-table td{height:33px;border-bottom:1px solid rgba(255,255,255,.8);vertical-align:middle;font-weight:300}
.hours-table td.day{width:157px;text-transform:uppercase;font-weight:400}
.hours-table tr:last-child td{border-bottom:none;vertical-align:top;padding-top:6px;line-height:20px}
.contact .foot-title{left:102px}
.contact-row{left:102px;display:flex;gap:18px;font-size:16.5px;line-height:21px;font-weight:300}
.contact-row svg{flex:none}
.follow{left:102px;top:232px;font-size:16px;font-weight:500}
.follow-links{left:102px;top:262px;display:flex;gap:12px;font-size:13px;font-weight:400}
</style>
</head>
<body>

<div class="topbar abs">
  <div class="info abs">
    <span><svg width="10" height="14" viewBox="0 0 10 14"><path d="M5 0a5 5 0 0 0-5 5c0 4 5 9 5 9s5-5 5-9a5 5 0 0 0-5-5zm0 7a2 2 0 1 1 0-4 2 2 0 0 1 0 4z" fill="#fff"/></svg>418 W. Harrow Lane, Suite 2C Pellbrook, IL 60999</span>
    <span><svg width="16" height="11" viewBox="0 0 16 11"><rect x=".5" y=".5" width="15" height="10" fill="none" stroke="#fff"/><path d="M.5.5 8 6l7.5-5.5" fill="none" stroke="#fff"/></svg>info@grinsofpellbrook.example</span>
  </div>
  <div class="social abs"><span>friendspace</span><span>chirper</span><span>picturegram</span></div>
</div>

<header class="header abs">
  <div class="brand abs"><span class="brand-dot"></span><span class="brand-name">Grins of Pellbrook</span></div>
  <div class="phone abs">
    <svg width="16" height="26" viewBox="0 0 16 26"><rect x="1" y="1" width="14" height="24" rx="2" fill="none" stroke="#1fc8c9" stroke-width="1.5"/><line x1="6" y1="21" x2="10" y2="21" stroke="#1fc8c9" stroke-width="1.5"/></svg>
    Call Us: 1-800-555-0142
  </div>
</header>

<nav class="nav abs">
  <a class="active" href="#">Home</a>
  <a href="#">About Us</a>
  <a href="#">Services</a>
  <a href="#">Our Team</a>
  <a href="#">Patient Education</a>
  <a href="#">Patient Forms</a>
  <a href="#">Contact</a>
</nav>

<section class="hero abs">
  <div class="hero-photo abs" role="img" aria-label="Smiling dentist in a white coat holding a green apple and a toothbrush"></div>
  <div class="hero-kicker abs">A Warm Welcome to You &amp; Your Family</div>
  <div class="hero-line abs" style="top:138px">Honestly Caring &amp;</div>
  <div class="hero-line abs" style="top:205px">Quality <strong>Dentistry</strong></div>
  <a class="btn btn-solid">Book Now</a>
  <a class="btn btn-ghost">Learn More</a>
  <div class="dots abs" style="left:166px;top:370px"><span class="dot on"></span><span class="dot"></span><span class="dot"></span></div>
</section>

<h2 class="section-title why-title abs">Why <strong>Choose Us</strong></h2>
<p class="section-sub why-sub abs">Let us brighten your smile!</p>

<div class="feature abs" style="left:115px">
  <svg viewBox="0 0 60 62"><circle cx="30" cy="31" r="26" fill="none" stroke="#6a2ff2" stroke-width="2"/><path d="M19 32l8 8 15-17" fill="none" stroke="#6a2ff2" stroke-width="2.4"/></svg>
  Highly trained<br>dental team
</div>
<div class="feature abs" style="left:339px">
  <svg viewBox="0 0 60 62"><path d="M14 6c-8 3-9 14-6 24 2 7 3 14 5 22 1 5 6 5 7 0l3-12c1-4 13-4 14 0l3 12c1 5 6 5 7 0 2-8 3-15 5-22 3-10 2-21-6-24-6-2-11 1-16 1S20 4 14 6z" fill="none" stroke="#6a2ff2" stroke-width="2"/></svg>
  Extensive line of<br>dental services
</div>
<div class="feature abs" style="left:587px">
  <svg viewBox="0 0 60 62"><line x1="10" y1="6" x2="46" y2="52" stroke="#6a2ff2" stroke-width="2"/><rect x="36" y="40" width="12" height="18" rx="3" transform="rotate(-38 42 49)" fill="none" stroke="#6a2ff2" stroke-width="2"/><circle cx="10" cy="6" r="4" fill="none" stroke="#6a2ff2" stroke-width="2"/></svg>
  Advanced dental<br>treatment facilities and<br>equipment
</div>
<div class="feature abs" style="left:846px">
  <svg viewBox="0 0 60 62"><path d="M14 6c-8 3-9 14-6 24 2 7 3 14 5 22 1 5 6 5 7 0l3-12c1-4 13-4 14 0l3 12c1 5 6 5 7 0 2-8 3-15 5-22 3-10 2-21-6-24-6-2-11 1-16 1S20 4 14 6z" fill="none" stroke="#6a2ff2" stroke-width="2"/><path d="M38 14v8M34 18h8" stroke="#6a2ff2" stroke-width="2"/></svg>
  Guaranteed results<br>and brighter smiles
</div>

<section class="doctor abs">
  <div class="doctor-photo abs" role="img" aria-label="Portrait of the lead dentist in a dark suit"></div>
  <h2 class="doctor-title abs">Meet <strong>Dr. Anjali Moreno, DDS</strong></h2>
  <div class="doctor-text abs">
    <p>Dr. Anjali Moreno provides a full range of dental services to the whole family. Many of our patient families span multiple generations. Our Team are dedicated to taking the time needed to provide the very best care every patient deserves.</p>
    <p>New patients looking for quality dental care in a relaxed environment are welcome! We accept PPO, Indeminity and Traditional Insurance plans.</p>
  </div>
  <a class="btn btn-team">Meet Our Awesome Team</a>
</section>

<h2 class="section-title happy-title abs">Our <strong>Happy Patients</strong></h2>
<p class="section-sub happy-sub abs">Smiles to be proud of!</p>

<article class="quote quote-purple abs">
  <div class="quote-mark">&ldquo;</div>
  <p>Lorem ipsum dolor sit amet, consectetur adipiscing elit, sed do eiusmod tempor incididunt ut labore et dolore magna aliqua. Ut enim ad minim veniam, quis nostrud exercitation.</p>
  <div class="who"><div class="avatar" role="img" aria-label="Patient portrait"></div><div><b>MARCO ELLIS DANE</b><small>Happy Patient</small></div></div>
</article>
<article class="quote quote-outline abs">
  <div class="quote-mark">&ldquo;</div>
  <p>Lorem ipsum dolor sit amet, consectetur adipiscing elit, sed do eiusmod tempor incididunt ut labore et dolore magna aliqua. Ut enim ad minim veniam, quis nostrud exercitation.</p>
  <div class="who"><div class="avatar" role="img" aria-label="Patient portrait"></div><div><b style="color:#333">MARCO ELLIS DANE</b><small>Happy Patient</small></div></div>
</article>
<div class="dots happy-dots abs"><span class="dot on"></span><span class="dot"></span><span class="dot"></span></div>

<footer>
  <section class="hours abs">
    <h3 class="foot-title abs">Clinic <strong>Hours</strong></h3>
    <table class="hours-table abs">
      <tr><td class="day">Monday</td><td>12:00pm to 6:00pm</td></tr>
      <tr><td class="day">Tuesday</td><td>10:00am to 7:00pm</td></tr>
      <tr><td class="day">Wednesday</td><td>Closed</td></tr>
      <tr><td class="day">Thursday</td><td>8:00am to 6:00pm</td></tr>
      <tr><td class="day">Friday</td><td>8:00am to 5:00pm</td></tr>
      <tr><td class="day">Saturday</td><td>8:00am to 3:00pm /<br>8:00am to 12:00pm</td></tr>
    </table>
  </section>
  <section class="contact abs">
    <h3 class="foot-title abs">Contact <strong>Us Now</strong></h3>
    <div class="contact-row abs" style="top:111px">
      <svg width="26" height="18" viewBox="0 0 26 18"><rect x="1" y="1" width="24" height="16" fill="#fff"/><path d="M1 1l12 9 12-9" fill="none" stroke="#6a2ff2" stroke-width="1.5"/></svg>
      info@grinsofpellbrook.example
    </div>
    <div class="contact-row abs" style="top:151px">
      <svg width="26" height="24" viewBox="0 0 26 24"><path d="M13 1a8 8 0 0 0-8 8c0 6 8 14 8 14s8-8 8-14a8 8 0 0 0-8-8zm0 11a3 3 0 1 1 0-6 3 3 0 0 1 0 6z" fill="#fff"/></svg>
      <span>418 W. Harrow Lane, Suite 2C<br>Pellbrook, IL 60999</span>
    </div>
    <div class="follow abs">Follow Us!</div>
    <div class="follow-links abs"><span>friendspace</span><span>chirper</span><span>picturegram</span></div>
  </section>
</footer>

</body>
</html>
```